Brookfell Self Storage - Business Sign

The sign we are needing designed is our main road sign for our self-storage business. The dimensions of the sign are 57 inches tall x 96 inches wide. We require that our attached logo be on the sign as well as our phone number: 478-216-4387 and website www.BrookfellStorage.net. Optional information that can be added but not required is our address: 418 Marlow Tenney Pkwy, Centerville, GA 31047.

Industry/Entity Type

Self Storage

Font styles to use
Sans Serif

```html
<!DOCTYPE html>
<html lang="en">
<head>
<meta charset="utf-8">
<title>Brookfell Self Storage – Road Sign</title>
<link rel="stylesheet" href="https://fonts.googleapis.com/css2?family=Arimo:wght@700&family=Barlow:wght@500&family=Open+Sans:wght@700&display=swap">
<style>
  :root {
    --page-bg: #f3f3f3;
    --sign-white: #ffffff;
    --brand-grey: #474747;
    --sky-blue: #4baefc;
    --steel-blue: #377fcb;
    --deep-blue: #025cb8;
    --shadow-blue: #0b4b98;
    --text-white: #ffffff;
  }
  html, body {
    margin: 0;
    padding: 0;
    width: 1200px;
    height: 851px;
    overflow: hidden;
    background: var(--page-bg);
  }
  .canvas {
    width: 1200px;
    height: 851px;
    display: flex;
    align-items: center;
    justify-content: center;
  }
  .sign {
    display: block;
    width: 1140px;
    height: 676px;
  }
  .sign__panel { fill: var(--sign-white); }
  .sign__roof-light { fill: var(--sky-blue); }
  .sign__roof-shade { fill: var(--steel-blue); }
  .sign__field { fill: var(--deep-blue); }
  .sign__web-band { fill: var(--sky-blue); }
  .brand-name {
    font-family: "Barlow", Arial, sans-serif;
    font-weight: 500;
    font-size: 150px;
    fill: var(--brand-grey);
    letter-spacing: 4px;
  }
  .phone {
    font-family: "Arimo", Arial, sans-serif;
    font-weight: 700;
    font-size: 190px;
  }
  .phone--shadow { fill: var(--shadow-blue); }
  .phone--main { fill: var(--text-white); }
  .website {
    font-family: "Open Sans", Arial, sans-serif;
    font-weight: 700;
    font-size: 82px;
    fill: var(--text-white);
    letter-spacing: 2px;
  }
</style>
</head>
<body>
<main class="canvas">
  <svg class="sign" viewBox="0 0 1912 1134" xmlns="http://www.w3.org/2000/svg" aria-label="Brookfell Self Storage road sign">
    <rect class="sign__panel" x="0" y="0" width="1912" height="1134"/>

    <text class="brand-name" x="956" y="340" text-anchor="middle">Brookfell Self Storage</text>

    <polygon class="sign__roof-light" points="0,725 956,555 956,1134 0,1134"/>
    <polygon class="sign__roof-shade" points="956,555 1912,725 1912,1134 956,1134"/>
    <polygon class="sign__field" points="0,772 956,602 1912,772 1912,1134 0,1134"/>

    <text class="phone phone--shadow" x="974" y="930" text-anchor="middle">478-216-4387</text>
    <text class="phone phone--main" x="956" y="912" text-anchor="middle">478-216-4387</text>

    <rect class="sign__web-band" x="0" y="975" width="1912" height="107"/>
    <text class="website" x="956" y="1058" text-anchor="middle">www.BrookfellStorage.net</text>
  </svg>
</main>
</body>
</html>
```